Brightwave Reach - Business Card

We need a business card for a Social Media Marketing company that specializes in online marketing for small businesses in Canada using common Social Media platforms such as Pictora, Kinloop, Vanishly & Chirpo.

I have uploaded a copy of our logo which I would like utilized in the business card. We would like the business card to be modern yet classy design.

Our website is www.brightwavereach.ca

Industry/Entity Type

Marketing

Contact Information for Business Card

Email: info@brightwavereach.ca
Website: www.brightwavereach.ca
Telephone: 604-392-5108

Colors

Designer to choose colors to be used in the design.

Requirements
Must have
• Social Media icons on reverse
• Please add some designs with color.

```html
<!DOCTYPE html>
<html lang="en">
<head>
<meta charset="utf-8">
<title>Brightwave Reach – Business Card</title>
<link rel="stylesheet" href="https://fonts.googleapis.com/css2?family=Roboto+Condensed:wght@400;700&display=swap">
<style>
  :root {
    --backdrop: #efece6;
    --card-light: #ededed;
    --card-dark: #3d4143;
    --ink-dark: #3d4143;
    --ink-light: #f4f4f4;
    --edge-mid: #8a8d8f;
  }
  * { box-sizing: border-box; margin: 0; padding: 0; }
  html, body {
    width: 1131px;
    height: 1200px;
    overflow: hidden;
    background: var(--backdrop);
    font-family: "Roboto Condensed", "Arial Narrow", sans-serif;
  }
  .canvas {
    position: relative;
    width: 1131px;
    height: 1200px;
  }
  .card {
    position: absolute;
    left: 135px;
    width: 860px;
    height: 490px;
    display: flex;
    box-shadow: 0 8px 22px rgba(0,0,0,0.18);
    overflow: hidden;
  }
  .card--front { top: 70px; background: var(--card-light); }
  .card--back  { top: 640px; background: var(--card-dark); }

  .card__main {
    flex: 1;
    display: flex;
    flex-direction: column;
    align-items: center;
    justify-content: center;
  }

  .card__edge {
    width: 26px;
    flex: none;
  }
  .card--front .card__edge {
    background: linear-gradient(90deg, var(--card-light), var(--edge-mid) 45%, var(--card-dark));
  }
  .card--back .card__edge {
    background: linear-gradient(90deg, var(--card-dark), var(--edge-mid) 55%, var(--card-light));
  }

  .card__strip {
    list-style: none;
    width: 150px;
    flex: none;
    display: flex;
    flex-direction: column;
    justify-content: space-evenly;
    align-items: center;
    padding: 40px 0;
  }
  .card--front .card__strip { background: var(--card-dark); color: var(--ink-light); }
  .card--back  .card__strip { background: var(--card-light); color: var(--ink-dark); }

  .platform {
    font-size: 22px;
    font-weight: 700;
    letter-spacing: 0.5px;
  }

  .brand-name {
    font-weight: 700;
    text-transform: uppercase;
    text-align: center;
    line-height: 0.95;
    letter-spacing: 1px;
  }
  .card--front .brand-name {
    color: var(--ink-dark);
    font-size: 80px;
    border: 6px solid var(--ink-dark);
    padding: 26px 34px;
  }
  .card--back .brand-name {
    color: var(--ink-light);
    font-size: 40px;
    border: 3px solid var(--ink-light);
    padding: 14px 18px;
  }

  .website {
    margin-top: 44px;
    font-size: 27px;
    font-weight: 700;
    color: var(--ink-dark);
  }

  .contact {
    list-style: none;
    margin-top: 56px;
    color: var(--ink-light);
    font-size: 27px;
  }
  .contact__item {
    display: flex;
    align-items: center;
    gap: 20px;
    margin-bottom: 14px;
  }
  .contact__icon {
    width: 30px;
    height: 30px;
    flex: none;
  }
</style>
</head>
<body>
<main class="canvas">

  <section class="card card--front" aria-label="Card front">
    <div class="card__main">
      <h1 class="brand-name">Brightwave<br>Reach</h1>
      <p class="website">www.brightwavereach.ca</p>
    </div>
    <div class="card__edge" role="img" aria-label="Distressed grunge texture edge"></div>
    <ul class="card__strip" aria-label="Social platforms">
      <li class="platform">Kinloop</li>
      <li class="platform">Chirpo</li>
      <li class="platform">Pictora</li>
      <li class="platform">Vanishly</li>
    </ul>
  </section>

  <section class="card card--back" aria-label="Card back">
    <div class="card__main">
      <h2 class="brand-name">Brightwave<br>Reach</h2>
      <ul class="contact">
        <li class="contact__item">
          <svg class="contact__icon" viewBox="0 0 30 30" aria-hidden="true">
            <rect x="2" y="7" width="26" height="17" fill="none" stroke="#f4f4f4" stroke-width="2.4"/>
            <polyline points="2,7 15,17 28,7" fill="none" stroke="#f4f4f4" stroke-width="2.4"/>
          </svg>
          <span>info@brightwavereach.ca</span>
        </li>
        <li class="contact__item">
          <svg class="contact__icon" viewBox="0 0 30 30" aria-hidden="true">
            <path d="M8 3 L12 3 L14 9 L11 11 Q13 17 19 20 L21 17 L27 19 L27 23 Q26 27 22 27 Q10 25 4 10 Q4 5 8 3 Z" fill="#f4f4f4"/>
          </svg>
          <span>604-392-5108</span>
        </li>
        <li class="contact__item">
          <svg class="contact__icon" viewBox="0 0 30 30" aria-hidden="true">
            <g fill="none" stroke="#f4f4f4" stroke-width="2.2">
              <circle cx="15" cy="15" r="12"/>
              <ellipse cx="15" cy="15" rx="5.5" ry="12"/>
              <line x1="3" y1="15" x2="27" y2="15"/>
              <line x1="5" y1="9" x2="25" y2="9"/>
              <line x1="5" y1="21" x2="25" y2="21"/>
            </g>
          </svg>
          <span>www.brightwavereach.ca</span>
        </li>
      </ul>
    </div>
    <div class="card__edge" role="img" aria-label="Distressed grunge texture edge"></div>
    <ul class="card__strip" aria-label="Social platforms">
      <li class="platform">Kinloop</li>
      <li class="platform">Chirpo</li>
      <li class="platform">Pictora</li>
      <li class="platform">Vanishly</li>
    </ul>
  </section>

</main>
</body>
</html>
```